Sports Betting Business Consultant

After 21 years in corporate life. Will be continue as consultant/advisor in sports betting industry. Need a business card. Prefer an Zelvo format as layout. Elements; betting,ticket, sports types soccer, basketball, tennis etc , odds etc.

```html
<!DOCTYPE html>
<html lang="en">
<head>
<meta charset="utf-8">
<title>Deniz Arvel – Business Card</title>
<link rel="stylesheet" href="https://fonts.googleapis.com/css2?family=Archivo:wght@800&family=Jost:wght@400&display=swap">
<style>
  :root {
    --backdrop: #0b0b0b;
    --card: #f5f5f3;
    --accent-blue: #5b7fa0;
    --accent-grey: #6a6a6a;
    --text-grey: #5e5e5e;
  }
  html, body {
    margin: 0;
    width: 1200px;
    height: 900px;
    overflow: hidden;
    background: var(--backdrop);
  }
  .business-card {
    position: absolute;
    left: 180px;
    top: 210px;
    width: 840px;
    height: 480px;
    background: var(--card);
    overflow: hidden;
  }
  .top-rule {
    position: absolute;
    top: 22px;
    left: 187px;
    width: 556px;
    height: 10px;
    background: linear-gradient(to right, var(--accent-grey) 0 48%, var(--accent-blue) 48% 100%);
  }
  .corner-bar {
    position: absolute;
    bottom: 0;
    height: 10px;
  }
  .corner-bar--left { left: 0; width: 116px; background: var(--accent-grey); }
  .corner-bar--right { right: 0; width: 120px; background: var(--accent-blue); }
  .identity {
    position: absolute;
    top: 50%;
    left: 188px;
    transform: translateY(-50%);
    display: flex;
    align-items: center;
    gap: 24px;
  }
  .holder-name {
    font-family: "Archivo", "Arial Black", sans-serif;
    font-weight: 800;
    font-size: 34px;
    letter-spacing: 0.2px;
    color: var(--accent-blue);
    margin: 0;
    position: relative;
    top: -8px;
  }
  .divider {
    width: 6px;
    height: 56px;
    background: var(--accent-grey);
  }
  .contact {
    font-family: "Jost", "Futura", sans-serif;
    font-size: 23px;
    letter-spacing: 2px;
    line-height: 1.1;
    color: var(--text-grey);
    margin: 0;
  }
</style>
</head>
<body>
  <section class="business-card">
    <div class="top-rule"></div>
    <div class="identity">
      <h1 class="holder-name">Deniz Arvel</h1>
      <div class="divider"></div>
      <p class="contact">+90 555 014 2290<br>dnzarv@postmail.com</p>
    </div>
    <div class="corner-bar corner-bar--left"></div>
    <div class="corner-bar corner-bar--right"></div>
  </section>
</body>
</html>
```